Poster Design to promote Adult Group Guitar Classes for Music School

We're a young music school trying to promote our Grown-Up Strum Starter Series classes, and need an eye catching poster design to promote the course. We'll be wanting to put the posters up on telegraph poles, community notice boards, shop front windows, cafes, shops and the around the general area of Sydney's Inner West, plus be able to covert it as a jpg image which we can forward to our mailing list and post on our website.

The poster should be visually appealing and incorporate images of what we are trying to promote.

We'd like the design to be professional, fun, creative and compliment our current logo design and colours.

Be sure to highlight 'Register Now'

Text to be used as follows:

STRUM STARTER SERIES CLASSES
For Beginner Adults

NEWTOWN

8 week Jam Packed Course
Small Groups (max. 6 people)
Guitars provided on site
Weekly hour long classes
Perfect introduction to learning the fundamentals
Materials Included
No music experience required

RESGISTER NOW – Limited Spaces
Visit our website for class times and start dates
www.brightreedmusic.com.au

T: (02) 7413 2958
E: info@brightreedmusic.com.au

PRIVATE MUSIC TUITION | ENSEMBLE | GROUP | GLEE CLUB

Industry/Entity Type

School

Requirements
Must have
• Bright Reed Music Logo

A3 poster size

Be in a print ready file for off-set printing. CMYK with 3mm bleed

```html
<!DOCTYPE html>
<html lang="en">
<head>
<meta charset="utf-8">
<title>Strum Starter Series Classes – Bright Reed Music</title>
<link rel="stylesheet" href="https://fonts.googleapis.com/css2?family=Ubuntu:wght@400;500;700&display=swap">
<style>
  :root {
    --orange: #f07a2a;
    --teal: #5bc3d0;
    --teal-wash: #cfeaf0;
    --paper: #ffffff;
    --stage: #e8e5e1;
    --photo-warm: #d9b48f;
    --photo-dark: #3a3d4a;
  }
  * { box-sizing: border-box; margin: 0; padding: 0; }
  html, body {
    width: 1200px; height: 900px; overflow: hidden;
    background: var(--stage);
    font-family: "Ubuntu", Arial, sans-serif;
  }
  .poster {
    position: absolute; left: 305px; top: 33px;
    width: 590px; height: 834px; overflow: hidden;
    background:
      radial-gradient(ellipse 60% 35% at 80% 20%, var(--teal-wash), transparent 70%),
      radial-gradient(ellipse 55% 30% at 15% 55%, var(--teal-wash), transparent 70%),
      radial-gradient(ellipse 50% 30% at 85% 70%, #e3f3f6, transparent 70%),
      var(--paper);
    box-shadow: 0 6px 18px rgba(0,0,0,.18);
  }
  .headline-small {
    position: absolute; left: 19px; top: 28px;
    color: var(--teal); font-size: 50px; font-weight: 500; letter-spacing: 1px;
  }
  .headline-big {
    position: absolute; left: 12px; top: 62px;
    color: var(--orange); font-size: 122px; font-weight: 500; letter-spacing: -3px; line-height: 1;
  }
  .headline-row {
    position: absolute; left: 0; top: 196px; display: flex; align-items: flex-end;
  }
  .series-band {
    background: var(--teal); color: var(--paper);
    font-size: 58px; font-weight: 700; padding: 6px 14px 4px 18px; line-height: 1;
  }
  .classes-word {
    color: var(--orange); font-size: 70px; font-weight: 500; letter-spacing: -1px;
    line-height: 1; margin-left: 8px; margin-bottom: 10px;
  }
  .audience {
    position: absolute; right: 18px; top: 272px;
    color: var(--teal); font-size: 27px; font-weight: 500;
  }
  .location-band {
    position: absolute; left: 300px; top: 312px; width: 310px; height: 70px;
    background: var(--teal); transform: rotate(-4deg); transform-origin: left center;
    display: flex; align-items: center; padding-left: 22px;
    color: var(--paper); font-size: 46px; font-weight: 500; letter-spacing: 1px;
  }
  .photo {
    position: absolute; left: 30px; top: 360px; width: 350px; height: 440px;
    border-radius: 45% 45% 12% 12%;
    background:
      radial-gradient(ellipse 40% 28% at 40% 20%, var(--photo-warm), transparent 75%),
      radial-gradient(ellipse 60% 35% at 45% 85%, var(--photo-dark), transparent 75%),
      linear-gradient(180deg, #e9dccd, #c9c2b8);
    opacity: .85;
  }
  .features {
    position: absolute; left: 381px; top: 478px; width: 200px;
    list-style: none; color: var(--orange); font-size: 13.5px; line-height: 1.28;
  }
  .features li { padding-left: 12px; position: relative; }
  .features li::before {
    content: ""; position: absolute; left: 0; top: 6px;
    width: 5px; height: 5px; background: var(--orange); border-radius: 50%;
  }
  .register-band {
    position: absolute; left: -20px; top: 676px; width: 350px; height: 108px;
    background: var(--orange); transform: rotate(-8deg); transform-origin: left center;
    color: var(--paper); padding: 12px 0 0 38px;
  }
  .register-band .cta { font-size: 42px; font-weight: 700; line-height: 1; }
  .register-band .note { font-size: 28px; font-weight: 400; margin-top: 4px; }
  .brand {
    position: absolute; left: 400px; top: 700px; width: 170px;
    display: flex; flex-direction: column; align-items: center; gap: 6px;
  }
  .brand-dot { width: 44px; height: 44px; border-radius: 50%; background: var(--orange); }
  .brand-name { color: var(--teal); font-size: 19px; font-weight: 500; }
  .contact {
    position: absolute; left: 366px; top: 774px; width: 215px; color: var(--teal);
  }
  .contact .visit { font-size: 10px; }
  .contact .web { font-size: 15px; font-weight: 700; margin-top: 2px; }
  .contact .details { font-size: 9.5px; margin-top: 2px; }
  .services {
    position: absolute; left: 14px; top: 812px;
    color: var(--orange); font-size: 11px; font-weight: 500; letter-spacing: .3px;
  }
</style>
</head>
<body>
  <main class="poster">
    <div class="headline-small">STRUM</div>
    <div class="headline-big">STARTER</div>
    <div class="headline-row">
      <span class="series-band">SERIES</span>
      <span class="classes-word">CLASSES</span>
    </div>
    <div class="audience">For Beginner Adults</div>
    <div class="photo" role="img" aria-label="Photo of a young woman sitting cross-legged playing an acoustic guitar"></div>
    <div class="location-band">NEWTOWN</div>
    <ul class="features">
      <li>8 week Jam Packed Course</li>
      <li>Small Groups (max. 6 people)</li>
      <li>Guitars provided on site</li>
      <li>Weekly hour long classes</li>
      <li>Perfect introduction to learning the fundamentals</li>
      <li>Materials Included</li>
      <li>No music experience required</li>
    </ul>
    <div class="register-band">
      <div class="cta">REGISTER NOW</div>
      <div class="note">Limited Spaces</div>
    </div>
    <div class="brand">
      <span class="brand-dot"></span>
      <span class="brand-name">Bright Reed Music</span>
    </div>
    <div class="contact">
      <p class="visit">Visit our website for class times and start dates</p>
      <p class="web">www.brightreedmusic.com.au</p>
      <p class="details">T: (02) 7413 2958 &nbsp;E: info@brightreedmusic.com.au</p>
    </div>
    <div class="services">PRIVATE MUSIC TUITION | ENSEMBLE | GROUP | GLEE CLUB</div>
  </main>
</body>
</html>
```